Digital menu Skydiving company

Design Digital menu/pricelist for our company. It can have dynamic components. We are also looking for a Graphic design for all our projects. Our main goals are to look clean/sharp and professional. Information is in psd file

3 packages Amber Plunge, Harbor Voyage, And Thunder Journey. then we have addons and merchandise

Colors
0293ce
34a7d8
ffffff
fbee3f
3377b5
000000
f37122
ec1f27
e34197

Requirements
Must have
• Sorry If I couldn't get my vision across better, Please see really rough design idea attached. one large picture section that rotates through 3 or 4 pictures. then all the information down the bottom and on right (see menu pricelist attached)

```html
<!DOCTYPE html>
<html lang="en">
<head>
<meta charset="utf-8">
<title>Packages &amp; Pricing</title>
<link href="https://fonts.googleapis.com/css2?family=Montserrat:wght@300;400;700;800&display=swap" rel="stylesheet">
<style>
  :root {
    --page-bg: #d9dadc;
    --panel-black: #121212;
    --panel-grey: #4a4a4c;
    --sky-blue: #3db0e4;
    --navy: #2b3794;
    --royal: #2f73d4;
    --tagline: #3aa8de;
    --white: #ffffff;
    --text-light: #e6e6e6;
    --divider: #5a5a5a;
  }
  * { box-sizing: border-box; margin: 0; padding: 0; }
  html, body {
    width: 1200px; height: 803px; overflow: hidden;
    background: var(--page-bg);
    font-family: "Montserrat", sans-serif;
  }
  .menu-board {
    position: absolute; left: 20px; top: 75px;
    width: 1160px; height: 653px;
    background: var(--white);
  }
  .hero-photo {
    position: absolute; left: 0; top: 0; width: 850px; height: 332px;
    background: linear-gradient(180deg, #2a5fb8 0%, #3f82d4 55%, #7aa6d6 72%, #7a5a62 86%, #3c4f86 100%);
  }
  .hero-title {
    position: absolute; left: 0; width: 850px; top: 255px;
    text-align: center; color: var(--white);
    font-weight: 800; font-size: 51px; letter-spacing: 1px;
    text-shadow: 0 3px 8px rgba(0,0,0,.45);
  }
  .merch-photo {
    position: absolute; left: 850px; top: 0; width: 310px; height: 332px;
    background: radial-gradient(circle at 60% 50%, #d8e4f4 0%, #efefef 60%);
  }
  .packages-panel {
    position: absolute; left: 0; top: 344px; width: 850px; height: 309px;
    background: radial-gradient(ellipse at 50% 45%, var(--panel-grey) 0%, #262627 55%, var(--panel-black) 100%);
    overflow: hidden;
  }
  .canyon-photo {
    position: absolute; left: 859px; top: 344px; width: 301px; height: 309px;
    background: linear-gradient(170deg, #9ea8b6 0%, #a9a3a6 25%, #8a6a60 55%, #6d5a55 80%, #5c4c48 100%);
  }
  .column-divider {
    position: absolute; top: 24px; width: 1px; height: 257px; background: var(--divider);
  }
  .package { position: absolute; top: 0; width: 244px; height: 309px; }
  .package-header {
    position: absolute; top: 23px; left: 0; width: 244px; height: 44px;
    display: flex; flex-direction: column; justify-content: center; align-items: center;
    color: var(--white); font-weight: 700; font-size: 16px; line-height: 18.5px;
    text-transform: uppercase; text-align: center;
  }
  .package--amber .package-header { background: var(--sky-blue); }
  .package--harbor .package-header { background: var(--navy); }
  .package--thunder .package-header { background: var(--royal); }
  .package-tagline {
    position: absolute; top: 86px; left: 0; width: 244px;
    color: var(--tagline); font-size: 13px; font-weight: 400; text-align: center; white-space: nowrap;
  }
  .package--harbor .package-tagline { text-align: left; }
  .feature-list { position: absolute; top: 121px; left: 0; width: 244px; list-style: none; }
  .feature-list li {
    position: relative; padding-left: 14px; color: var(--white);
    font-weight: 700; font-size: 10.5px; line-height: 11.5px; text-transform: uppercase;
    display: flex; justify-content: space-between; align-items: flex-end;
  }
  .feature-list--spaced li { margin-bottom: 11.5px; }
  .feature-list--tight li { margin-bottom: 4.5px; }
  .feature-list li::before {
    content: ""; position: absolute; left: 0; top: 1px;
    width: 9px; height: 9px; border-radius: 50%; background: #2f8fd6;
  }
  .feature-list li::after {
    content: ""; position: absolute; left: 2px; top: 4px;
    width: 3px; height: 3px; border-top: 1.5px solid var(--white); border-right: 1.5px solid var(--white);
    transform: rotate(45deg);
  }
  .feature-price { padding-right: 4px; }
  .merch-list { position: absolute; top: 164px; left: 0; width: 244px; list-style: none; }
  .merch-list li {
    display: flex; justify-content: space-between;
    color: var(--text-light); font-weight: 300; font-size: 12.5px; line-height: 15.8px;
  }
  .price-tab {
    position: absolute; top: 273px; width: 131px; height: 36px;
    border-radius: 22px 22px 0 0; color: var(--white);
    font-weight: 800; font-size: 21px; text-align: center; line-height: 36px;
  }
  .package--amber .price-tab { left: 55px; background: var(--sky-blue); }
  .package--harbor .price-tab { left: 57px; background: var(--navy); }
  .package--thunder .price-tab { left: 59px; background: var(--royal); }
</style>
</head>
<body>
  <main class="menu-board">
    <div class="hero-photo" role="img" aria-label="Tandem skydivers in free fall above a wide canyon under a deep blue sky"></div>
    <h1 class="hero-title">PACKAGES &amp; PRICING</h1>
    <div class="merch-photo" role="img" aria-label="Merchandise display of blue t-shirts, black hoodie, goggles and sneakers"></div>

    <section class="packages-panel">
      <div class="column-divider" style="left:283px"></div>
      <div class="column-divider" style="left:567px"></div>

      <article class="package package--amber" style="left:19px">
        <h2 class="package-header"><span>Amber Plunge</span><span>16,000FT</span></h2>
        <p class="package-tagline">THE SKYDIVE IS NAKED, NOT YOU...</p>
        <ul class="feature-list feature-list--tight">
          <li>Tandem skydive from 16,000ft MSL</li>
          <li>Certificate of achievement</li>
        </ul>
        <ul class="merch-list">
          <li><span>T-Shirt Short Sleeve</span><span>$20</span></li>
          <li><span>T-Shirt Long Sleeve</span><span>$28</span></li>
          <li><span>Sweat Shirts</span><span>$30</span></li>
          <li><span>Hoodies</span><span>$38</span></li>
          <li><span>Goggles from</span><span>$12</span></li>
        </ul>
        <div class="price-tab">$329</div>
      </article>

      <article class="package package--harbor" style="left:303px">
        <h2 class="package-header"><span>Harbor Voyage</span><span>16,000FT</span></h2>
        <p class="package-tagline">SKYDIVE &amp; SHARE THE MEMORIES...</p>
        <ul class="feature-list feature-list--spaced" style="left:4px">
          <li>Tandem skydive from<br>16,000ft MSL</li>
          <li>Photos</li>
          <li>Videos</li>
          <li>Certificate of achievement</li>
        </ul>
        <div class="price-tab">$459</div>
      </article>

      <article class="package package--thunder" style="left:587px">
        <h2 class="package-header"><span>Thunder Journey</span><span>16,000FT</span></h2>
        <p class="package-tagline">FOR THE THRILL SEEKER...</p>
        <ul class="feature-list feature-list--spaced">
          <li><span>Tandem skydive from<br>16,000ft MSL</span><span class="feature-price">$319</span></li>
          <li><span>Photos</span><span class="feature-price">$99</span></li>
          <li><span>Videos</span><span class="feature-price">$99</span></li>
          <li><span>Extreme extras</span><span class="feature-price">$50</span></li>
          <li><span>Summit Skydive t-shirt</span></li>
          <li><span>Certificate of achievement</span></li>
        </ul>
        <div class="price-tab">$499</div>
      </article>
    </section>

    <div class="canyon-photo" role="img" aria-label="View from an aircraft wing strut over a vast red rock canyon"></div>
  </main>
</body>
</html>
```